Pellmore Heating & Air

I need a business card made for my company. I would like my new logo for Pellmore Heating and Air on the front and my Garage Door on the back.
Front to say -Heating & Air Conditioning , Mini Splits and Heat Pumps, Hydronic In-Floor Heat. Locally Owned and Operated! Licensed, Boned and Insured. Free Estimates on new equipment. 555-201-4837
KVB Back Card, change phone# to 555-318-6024. Remove Commercial and residential and fully sticked vans lines.

```html
<!DOCTYPE html>
<html lang="en">
<head>
<meta charset="utf-8">
<title>Pellmore Heating &amp; Air – Business Card</title>
<link href="https://fonts.googleapis.com/css2?family=Open+Sans:wght@400;600;800&display=swap" rel="stylesheet">
<style>
  :root{
    --red:#ea3127;
    --blue:#0f4f8c;
    --ink:#2a2a2a;
    --orange:#f07a3c;
    --white:#ffffff;
    --backdrop:#e9e9e9;
  }
  *{margin:0;padding:0;box-sizing:border-box}
  html,body{width:1200px;height:900px;overflow:hidden}
  body{
    background:var(--backdrop);
    font-family:"Open Sans",Arial,sans-serif;
    display:flex;flex-direction:column;align-items:center;justify-content:center;gap:28px;
  }
  .card{
    width:720px;height:411px;border-radius:26px;position:relative;overflow:hidden;
    box-shadow:0 6px 18px rgba(0,0,0,.18);
  }
  /* garage door side */
  .card--garage{background:var(--red);display:flex;align-items:center;justify-content:center}
  .garage-brand{display:flex;flex-direction:column;align-items:center;gap:14px}
  .garage-brand__name{
    color:var(--white);font-weight:800;font-size:54px;letter-spacing:2px;text-transform:uppercase;line-height:1.05;text-align:center;
  }
  .garage-brand__rule{width:520px;height:3px;background:var(--orange)}

  /* heating side */
  .card--heating{background:var(--white)}
  .heating-brand{
    position:absolute;left:46px;top:42px;
    color:var(--red);font-weight:800;font-size:44px;line-height:1.05;text-transform:uppercase;letter-spacing:1px;
  }
  .partner-brand{
    position:absolute;right:44px;top:44px;text-align:center;
  }
  .partner-brand__name{color:var(--blue);font-weight:800;font-size:20px;text-transform:uppercase;letter-spacing:1px;line-height:1.15}
  .partner-brand__rule{height:2px;background:var(--orange);margin-top:6px}

  .contact{position:absolute;left:0;top:196px}
  .contact__head{border-left:14px solid var(--red);padding-left:36px}
  .contact__name{color:var(--red);font-weight:800;font-size:26px;text-transform:uppercase;line-height:1.1}
  .contact__title{color:var(--blue);font-size:17px;line-height:1.3}
  .contact__address{padding-left:50px;margin-top:16px;color:var(--ink);font-size:17px;line-height:1.35}
  .contact__lines{padding-left:50px;margin-top:14px;list-style:none;color:var(--ink);font-size:16px;line-height:1.45}
  .contact__lines li{display:flex;align-items:center;gap:8px}
  .contact__lines svg{width:14px;height:14px;fill:var(--red);flex:none}

  .services{position:absolute;right:40px;top:176px;text-align:right}
  .services__head{color:var(--red);font-weight:800;font-size:24px;text-transform:uppercase;margin-bottom:4px}
  .services__list{list-style:none;color:var(--ink);font-size:16px;line-height:1.45}
</style>
</head>
<body>

  <section class="card card--garage">
    <div class="garage-brand">
      <div class="garage-brand__name">Kinvale Bay<br>Garage Door</div>
      <div class="garage-brand__rule"></div>
    </div>
  </section>

  <section class="card card--heating">
    <div class="heating-brand">Pellmore<br>Heating &amp; Air</div>

    <div class="partner-brand">
      <div class="partner-brand__name">Kinvale Bay<br>Garage Door</div>
      <div class="partner-brand__rule"></div>
    </div>

    <div class="contact">
      <div class="contact__head">
        <div class="contact__name">Daniel Ortiz</div>
        <div class="contact__title">Managing Director</div>
      </div>
      <div class="contact__address">4120 Larkspur Ave S<br>Fernbrook, MN 55990</div>
      <ul class="contact__lines">
        <li><svg viewBox="0 0 16 16" aria-hidden="true"><path d="M3 1h3l1.5 4-2 1.3a9 9 0 0 0 4.2 4.2L11 8.5l4 1.5v3a2 2 0 0 1-2 2A12 12 0 0 1 1 3a2 2 0 0 1 2-2z"/></svg>555-318-6024</li>
        <li><svg viewBox="0 0 16 16" aria-hidden="true"><path d="M1 3h14v10H1z M1 3l7 6 7-6" fill="none" stroke="#ea3127" stroke-width="1.8"/></svg>office@kinvalebay.example</li>
        <li><svg viewBox="0 0 16 16" aria-hidden="true"><circle cx="8" cy="8" r="6.5" fill="none" stroke="#ea3127" stroke-width="1.6"/><path d="M1.5 8h13M8 1.5c-3 3.5-3 9.5 0 13M8 1.5c3 3.5 3 9.5 0 13" fill="none" stroke="#ea3127" stroke-width="1.2"/></svg>www.kinvalebay.example</li>
      </ul>
    </div>

    <div class="services">
      <div class="services__head">Service</div>
      <ul class="services__list">
        <li>Heating &amp; Air Conditioning</li>
        <li>, Mini Splits and Heat Pumps</li>
        <li>, Hydronic In-Floor Heat.</li>
        <li>Locally Owned and Operated!</li>
        <li>Licensed, Boned and Insured.</li>
      </ul>
    </div>
  </section>

</body>
</html>
```